Data Analytics Irish company needs Stationery Design

We need a stationery design for our data analytics company based in Dublin called 'Numbryx': we develop innovative web-based corporate applications exploiting advanced Machine Learning and Data Mining techniques.
Like the animal that inspired our company name, the final design should communicate intelligence and passion; on the other hand, we want to keep the highest professional appeal.
We love our current logo and we have tried out several color variations: we prefer solutions (see the logo attached) with white design and dark backgrounds, but we will also be glad to see some designs that follow the colors of the palette of the attached web screenshot.

```html
<!DOCTYPE html>
<html lang="en">
<head>
<meta charset="utf-8">
<title>Numbryx Stationery</title>
<link href="https://fonts.googleapis.com/css2?family=Exo+2:wght@400&family=Tinos&display=swap" rel="stylesheet">
<style>
  :root {
    --paper: #ffffff;
    --charcoal: #272928;
    --flap: #2b2d2c;
    --flap-edge: #1c1d1c;
    --ink: #ffffff;
    --watermark: #3d3f3e;
    --shadow: rgba(0, 0, 0, 0.35);
  }
  * { box-sizing: border-box; margin: 0; padding: 0; }
  html, body {
    width: 1143px;
    height: 1200px;
    overflow: hidden;
    background: var(--paper);
  }
  .stationery {
    position: relative;
    width: 1143px;
    height: 1200px;
  }
  .business-card {
    position: absolute;
    left: 6px;
    top: 6px;
    width: 1131px;
    height: 566px;
    background: var(--charcoal);
    box-shadow: 0 4px 6px var(--shadow);
    color: var(--ink);
    overflow: hidden;
  }
  .brand-dot {
    position: absolute;
    border-radius: 50%;
    background: var(--ink);
  }
  .business-card .brand-dot {
    left: 110px;
    top: 40px;
    width: 210px;
    height: 210px;
  }
  .brand-name {
    font-family: "Exo 2", sans-serif;
    font-weight: 400;
    color: var(--ink);
    letter-spacing: 1px;
    line-height: 1;
  }
  .business-card .brand-name {
    position: absolute;
    left: 58px;
    top: 268px;
    font-size: 74px;
  }
  .contact {
    position: absolute;
    top: 440px;
    font-family: "Tinos", serif;
    font-size: 29px;
    line-height: 40px;
  }
  .contact-phone { left: 54px; }
  .contact-address { left: 762px; }

  .envelope {
    position: absolute;
    left: 6px;
    top: 626px;
    width: 1131px;
    height: 570px;
    background: var(--charcoal);
    box-shadow: 0 4px 6px var(--shadow);
    color: var(--ink);
    overflow: hidden;
  }
  .envelope-watermark {
    position: absolute;
    left: 670px;
    top: 130px;
    width: 460px;
    height: 460px;
    border-radius: 50%;
    background: var(--watermark);
  }
  .envelope-flap {
    position: absolute;
    left: 0;
    top: 0;
    width: 1131px;
    height: 140px;
  }
  .envelope .brand-dot {
    left: 536px;
    top: 16px;
    width: 60px;
    height: 60px;
  }
  .envelope .brand-name {
    position: absolute;
    left: 0;
    width: 100%;
    top: 88px;
    text-align: center;
    font-size: 28px;
  }
  .website {
    position: absolute;
    left: 0;
    width: 100%;
    bottom: 20px;
    text-align: center;
    font-family: "Tinos", serif;
    font-size: 22px;
  }
</style>
</head>
<body>
<main class="stationery">
  <section class="business-card">
    <div class="brand-dot" aria-hidden="true"></div>
    <div class="brand-name">Numbryx</div>
    <div class="contact contact-phone">
      <p>t: 555.555.5555</p>
      <p>f: 555.555.5555</p>
    </div>
    <div class="contact contact-address">
      <p>47 Larkfield Road,</p>
      <p>Ashby, CA 90417</p>
    </div>
  </section>

  <section class="envelope">
    <div class="envelope-watermark" role="img" aria-label="Large faint brand emblem decoration"></div>
    <svg class="envelope-flap" viewBox="0 0 1131 140" aria-hidden="true">
      <polygon points="0,0 1131,0 1105,138 26,138" fill="var(--flap-edge)"/>
      <polygon points="0,0 1131,0 1103,134 28,134" fill="var(--flap)"/>
    </svg>
    <div class="brand-dot" aria-hidden="true"></div>
    <div class="brand-name">Numbryx</div>
    <p class="website">www.numbryx.com</p>
  </section>
</main>
</body>
</html>
```